Web Design for couples website

About us:
Duoperks.sg is a new startup website that aims to suggest and promote activities for young couples. The site will feature a blog and a group deals page (i.e Flockbuy).

What we need:
We require a talented designer to design a theme for the website. The design must include at least the following:
1. Logo Design - A logo should be provided along with the website design. The design should match the overall design of the website (or vice versa). The logo should include the words "Duoperks.sg" or "Duoperks". Capitalisation of the alphabets are not critical.

2 - Home / Landing page
The layout of this page should be similar to the standard 2 / 3 column wordpress pages with an image slider on top to feature articles / deals. There should also be a column on the side to include widgets such as social networking and mailing list subscription, etc

3. Deals Listing Page
This page will have a listing of all current group deals, similar to that of Flockbuy. The layout can either have deals listed in 1 or 2 columns.

4. Past Deals Page - See references below

5. Deal Page
Detailed information page for each specific deal. This should include deal image, title, buy button, timer, social media buttons, two column text.

References for deal pages:
www.bargainvale.com.sg
http://www.everyoffernest.com.au/daily-deals
www.totalsavepacific.com
www.hugeswapzo.com

6. General page design for miscellaneous pages like "About", "Contact", etc.

The overall theme of the website should cater to an audience of 18-30 year old young adults. Preferably to have something less colourful and give the overall feel of class. This should cater generally to females but males as well, so less (or no)pink / red would be preferable. But don't let yourself get restricted by these requirements and feel free to let your creative juices flow!
Updates

Hi Designers,

Thank you for your submissions so far. I would like to point out that the deal listing page will only be a sub section of the page.  Would appreciate if priority was given to the main / landing page slider and 2 or 3 columns for articles below.

Other priority would be for the single deal design, where I'm more interested to have more unique buttons such as "buy now" and "time left" .

Also to note, only .PSD design file is required. No coding (HTML / CSS) is necessary and should also be friendly for developers to work with.

Hi Designers,

 
Please submit proposal designs based on requirements on landing page or deal listings page as these would be my main requirements for consideration.

Also, Do try to keep the theme clean and easy on the eyes. Overall, I'm looking for something that is simplistic and/or classy with elegance.

Target Market(s)

18 - 30 years old young adults interested in dating and activities for couples

Industry/Entity Type

Media

Requirements
Must have
• - Logo
- Home
- Deal Page (specific)
- General layout

```html
<!DOCTYPE html>
<html lang="en">
<head>
<meta charset="utf-8">
<title>Duoperks — Home</title>
<link href="https://fonts.googleapis.com/css2?family=Lora:wght@400;700&family=Arimo:wght@400;700&display=swap" rel="stylesheet">
<style>
:root{
  --pink:#c7094f;
  --pink-dark:#a8003e;
  --green:#8dbf2e;
  --green-dark:#6f9e1c;
  --text:#333;
  --meta:#9a9a9a;
  --rule:#e79ab8;
  --frame:#e6e6e6;
  --cream:#fbf9ee;
  --night:#050005;
}
*{box-sizing:border-box;margin:0;padding:0}
html,body{width:970px;height:1200px;overflow:hidden}
body{
  background:radial-gradient(ellipse 620px 420px at 50% 0,#9a1a6f 0,#5a0d44 40%,#1b0418 75%,var(--night) 100%);
  font-family:Arimo,Arial,sans-serif;color:var(--text);position:relative;
}
.page{position:absolute;left:161px;top:20px;width:648px;height:1147px;background:#fff}
.logo{position:absolute;left:20px;top:18px;display:flex;align-items:center;gap:10px;
  font-family:Lora,serif;font-size:31px;line-height:40px;color:var(--pink)}
.logo-mark{width:16px;height:16px;border-radius:50%;background:var(--pink)}
.nav{position:absolute;right:12px;top:27px;display:flex;gap:20px;list-style:none}
.nav a{font-family:Lora,serif;font-size:18px;line-height:24px;color:var(--pink);text-decoration:none}

.slider{position:absolute;left:15px;top:86px;width:417px;height:244px;border:3px solid #eee;overflow:hidden}
.slide-photo{width:100%;height:100%;background:linear-gradient(160deg,#c9d4c8 0,#a5b59a 35%,#8c9a78 60%,#cfc6a8 100%)}
.slider-dots{position:absolute;right:8px;top:8px;display:flex;gap:3px}
.slider-dots span{width:9px;height:9px;border-radius:50%;background:#e6a3bd}
.slider-dots span:first-child{background:var(--pink)}
.slide-caption{position:absolute;left:0;right:0;bottom:0;height:48px;background:rgba(255,255,255,.8);padding:5px 8px}
.slide-caption h2{font-family:Lora,serif;font-weight:400;font-size:17px;line-height:20px;color:var(--pink)}
.slide-caption p{font-size:10.5px;color:#444;margin-top:2px}

.posts{position:absolute;left:15px;top:341px;width:417px;list-style:none}
.post{border-top:1px dashed var(--rule);position:relative;padding:7px 0 0 0}
.post:last-child{border-bottom:1px dashed var(--rule)}
.thumb{position:absolute;left:2px;top:13px;width:156px;height:92px;border:3px solid #fff;box-shadow:0 0 0 1px var(--frame),0 1px 3px rgba(0,0,0,.15)}
.post-body{margin-left:173px}
.post h3{font-family:Lora,serif;font-weight:400;font-size:16.5px;line-height:19px;color:var(--pink)}
.meta{font-size:8.3px;line-height:10px;color:var(--meta);margin:2px 0 5px}
.post p{font-size:9.3px;line-height:12.7px;color:#333}
.more{display:inline-block;margin-top:5px;border:1px solid #ddd;padding:2px 6px;font-size:9.3px;line-height:12px;font-weight:700;color:var(--pink)}

.pager{position:absolute;left:0;right:0;top:1120px;padding-left:224px;display:flex;gap:3px;list-style:none}
.pager li{min-width:15px;height:15px;padding:0 3px;border:1px solid #ccc;font-size:8px;line-height:13px;text-align:center;color:#555;background:#f6f6f6}
.pager li.current{background:#555;color:#fff;border-color:#555}
.pager li.gap{border:0;background:none}

.sidebar{position:absolute;left:445px;top:86px;width:189px}
.search{display:flex;height:20px;width:189px}
.search input{flex:1 1 0;width:0;min-width:0;border:1px solid #ddd;height:20px}
.search button{flex:none;width:39px;height:20px;background:var(--pink);color:#fff;border:0;font-family:Arimo,Arial,sans-serif;font-size:9px}
.deal{margin-top:22px;background:var(--cream);border:1px solid #eee;height:201px;position:relative}
.deal-ribbon{position:absolute;left:-5px;right:-5px;top:-4px;height:24px;background:linear-gradient(var(--green),var(--green-dark));color:#fff;font-family:Lora,serif;font-size:16px;text-align:center;line-height:24px}
.deal-photo{position:absolute;left:19px;top:30px;width:162px;height:104px;border:3px solid #fff;background:linear-gradient(135deg,#e8e5e0,#bfb8ac 60%,#8f8a82)}
.deal-status{position:absolute;left:22px;top:122px;width:156px;height:12px;background:rgba(255,255,255,.85);font-size:8px;padding-left:3px;line-height:12px}
.deal-status b{color:var(--green-dark);font-weight:400}
.deal h4{position:absolute;left:18px;top:140px;font-family:Lora,serif;font-size:12.3px;line-height:15px;color:var(--green-dark);white-space:nowrap}
.deal p{position:absolute;left:18px;top:172px;font-size:9px;line-height:13px}

.mailing{margin-top:15px;border:4px solid #f0f0f0;padding:8px 10px 10px;height:188px}
.mailing-head{display:flex;align-items:center;gap:7px}
.mailing h4{font-family:Lora,serif;font-size:11.6px;white-space:nowrap}
.mailing p{font-size:9px;line-height:13px;margin:7px 0}
.mailing .field{display:block;border:1px solid #ccc;height:16px;font-size:9px;line-height:11px;padding:2px 5px;margin-bottom:5px;color:#333}
.subscribe{display:block;margin:8px auto 0;width:90px;height:22px;background:var(--pink);color:#fff;border:0;font-family:Lora,serif;font-weight:700;font-size:12px}

.social{margin-top:14px;border:1px solid #ccc;height:167px;padding:5px 7px}
.social-head{display:flex;gap:6px}
.social-square{width:22px;height:22px;background:#3b5998}
.social-head strong{font-size:9.5px;color:#3b5998}
.like{margin-top:3px;border:1px solid #ccc;font-size:8px;padding:0 4px;display:inline-block;background:#f2f2f2}
.social-count{font-size:7.5px;border-top:1px solid #ddd;margin-top:7px;padding-top:3px}
.fans{display:grid;grid-template-columns:repeat(4,32px);gap:3px 8px;margin-top:4px;list-style:none}
.fans li{font-size:6.5px;text-align:center;color:#666}
.fans span{display:block;height:30px;background:linear-gradient(#5a4a50,#2a2226);margin-bottom:2px}
.social-foot{font-size:7px;color:#666;border-top:1px solid #ddd;margin-top:5px;padding-top:3px}

.popular h3{font-family:Lora,serif;font-weight:400;font-size:16px;margin:18px 0 6px}
.popular ul{list-style:none}
.popular li{display:flex;gap:8px;border-bottom:1px dashed var(--rule);padding:6px 0;min-height:66px}
.pop-thumb{width:48px;height:48px;flex:none;border:2px solid #fff;box-shadow:0 0 0 1px var(--frame)}
.popular a{font-family:Lora,serif;font-size:11px;line-height:14px;color:var(--pink);text-decoration:none}
.popular .meta{font-size:7.5px;margin:2px 0 0;line-height:10px}

.footer{position:absolute;left:161px;top:1173px;width:648px;display:flex;justify-content:space-between;font-size:8px;color:#fff}
</style>
</head>
<body>
<div class="page">
  <div class="logo"><span class="logo-mark"></span>Duoperks</div>
  <ul class="nav">
    <li><a href="#">Home</a></li><li><a href="#">About</a></li><li><a href="#">Blog</a></li><li><a href="#">Deals</a></li><li><a href="#">Contact</a></li>
  </ul>

  <section class="slider">
    <div class="slide-photo" role="img" aria-label="Smiling couple with backpacks leaning on a fence above a green coastal valley"></div>
    <div class="slider-dots"><span></span><span></span><span></span><span></span></div>
    <div class="slide-caption">
      <h2>A unique kind of journey:</h2>
      <p>Couple hiking across the country to bring awareness to issues facing millions</p>
    </div>
  </section>

  <ul class="posts">
    <li class="post" style="height:125px">
      <div class="thumb" role="img" aria-label="Bride and groom standing together outdoors" style="background:linear-gradient(135deg,#5a3f6a,#b8a080 55%,#ece6de)"></div>
      <div class="post-body">
        <h3>First Look: Do or Don't?</h3>
        <div class="meta">March 16th, 2012 11:32 &nbsp;// &nbsp;duoperks &nbsp;// &nbsp;5 comments</div>
        <p>While some couples stick with tradition and don't get a glimpse of each other on their wedding day until the bride appears at the top of the aisle, others choose to see each other before their ceremony.</p>
        <span class="more">Read more »</span>
      </div>
    </li>
    <li class="post" style="height:126px">
      <div class="thumb" role="img" aria-label="Vintage sepia wedding photograph" style="background:linear-gradient(135deg,#5e564a,#a69c8a 55%,#d8d0c0)"></div>
      <div class="post-body">
        <h3>Couple Gets Same $16.50 Hotel Rate From 1952 Wedding Night</h3>
        <div class="meta">March 16th, 2012 11:32 &nbsp;// &nbsp;duoperks &nbsp;// &nbsp;5 comments</div>
        <p>Amazing -- 60 years after they tied the knot, Connecticut couple Arthur and Ellen Marsh are returning this weekend to the special room.</p>
        <span class="more">Read more »</span>
      </div>
    </li>
    <li class="post" style="height:122px">
      <div class="thumb" role="img" aria-label="Couple embracing in a bright bedroom" style="background:linear-gradient(135deg,#3a2a28,#b48a70 55%,#e4ddd6)"></div>
      <div class="post-body">
        <h3>Top tips for a dirty weekend</h3>
        <div class="meta">March 16th, 2012 11:32 &nbsp;// &nbsp;duoperks &nbsp;// &nbsp;5 comments</div>
        <p>Planning a dirty weekend away with your partner? You'll both enjoy it far more if you do a little preparation...</p>
        <span class="more">Read more »</span>
      </div>
    </li>
    <li class="post" style="height:135px">
      <div class="thumb" role="img" aria-label="Couple kissing in warm golden sunlight" style="background:linear-gradient(135deg,#f2d6a0,#d9a870 50%,#9a7a5a)"></div>
      <div class="post-body">
        <h3>Are You the One for Me? Knowing Who's Right and Avoiding Who's Wrong</h3>
        <div class="meta">March 16th, 2012 11:32 &nbsp;// &nbsp;duoperks &nbsp;// &nbsp;5 comments</div>
        <p>Here is the book you've been waiting for to help you choose and keep the right partner.</p>
        <span class="more">Read more »</span>
      </div>
    </li>
    <li class="post" style="height:125px">
      <div class="thumb" role="img" aria-label="Two people in an office scene from a television show" style="background:linear-gradient(135deg,#7a8a90,#c8c4b4 55%,#e8e4dc)"></div>
      <div class="post-body">
        <h3>Best TV couples of all time</h3>
        <div class="meta">March 16th, 2012 11:32 &nbsp;// &nbsp;duoperks &nbsp;// &nbsp;5 comments</div>
        <p>From Lola and Rudy to "Starwatching"'s" Daniel and Mabel, we've highlighted 20 TV couples who've had the sexiest, zaniest and most romantic chemistry to ever grace the small screen.</p>
        <span class="more">Read more »</span>
      </div>
    </li>
    <li class="post" style="height:127px">
      <div class="thumb" role="img" aria-label="Two people in an office scene from a television show" style="background:linear-gradient(135deg,#7a8a90,#c8c4b4 55%,#e8e4dc)"></div>
      <div class="post-body">
        <h3>Best TV couples of all time</h3>
        <div class="meta">March 16th, 2012 11:32 &nbsp;// &nbsp;duoperks &nbsp;// &nbsp;5 comments</div>
        <p>From Lola and Rudy to "Starwatching"'s" Daniel and Mabel, we've highlighted 20 TV couples who've had the sexiest, zaniest and most romantic chemistry to ever grace the small screen.</p>
        <span class="more">Read more »</span>
      </div>
    </li>
  </ul>

  <ul class="pager">
    <li>‹</li><li>1</li><li>2</li><li>3</li><li class="current">4</li><li>5</li><li class="gap">...</li><li>10</li><li>20</li><li>30</li><li>›</li>
  </ul>

  <aside class="sidebar">
    <form class="search"><input type="text" aria-label="Search"><button type="button">Search</button></form>

    <section class="deal">
      <div class="deal-ribbon">Deal of the day!</div>
      <div class="deal-photo" role="img" aria-label="Bright hotel room with a sea view"></div>
      <div class="deal-status">125 bought. Deal is on! <b>Check out »</b></div>
      <h4>Isle of Wren:<br>Two Night 5* Stay For Two</h4>
      <p>With Golden Ladle Breakfast for $280<br>at The Harbourview (Up to 50% Off)</p>
    </section>

    <section class="mailing">
      <div class="mailing-head">
        <svg width="30" height="24" viewBox="0 0 34 26" aria-hidden="true"><rect x="1" y="3" width="32" height="22" fill="#fff" stroke="#9aa" /><path d="M1 3 L17 15 L33 3" fill="none" stroke="#9aa"/><rect x="24" y="5" width="7" height="6" fill="var(--pink)"/></svg>
        <h4>Join our mailing list</h4>
      </div>
      <p>Join over 400000 subscribers who receive our email newsletters.<br>Latest articles and deals right into your inbox!</p>
      <span class="field">Your name...</span>
      <span class="field">Your e-mail...</span>
      <button class="subscribe" type="button">Subscribe</button>
    </section>

    <section class="social">
      <div class="social-head"><span class="social-square"></span><div><strong>Circlepage Platform</strong><br><span class="like">Like</span></div></div>
      <div class="social-count">4,515,187 people like <b>Circlepage Platform</b>.</div>
      <ul class="fans">
        <li><span></span>Ines</li><li><span></span>Milo</li><li><span></span>Rana</li><li><span></span>Marek</li>
        <li><span></span>Soren</li><li><span></span>Adam</li><li><span></span>Rosa</li><li><span></span>Jude</li>
      </ul>
      <div class="social-foot">Circlepage social plugin</div>
    </section>

    <section class="popular">
      <h3>Popular posts</h3>
      <ul>
        <li><div class="pop-thumb" role="img" aria-label="Pink cocktails" style="background:linear-gradient(135deg,#f7c6d6,#e07aa0)"></div><div><a href="#">Lorem ipsum dolor sit</a><div class="meta">March 16th, 2012 11:32 //<br>duoperks // 5 comments</div></div></li>
        <li><div class="pop-thumb" role="img" aria-label="Cosy cafe interior" style="background:linear-gradient(135deg,#6a5040,#c0a888)"></div><div><a href="#">Proin consequat commodo mauris eu ornare.</a><div class="meta">March 16th, 2012 11:32 //<br>duoperks // 5 comments</div></div></li>
        <li><div class="pop-thumb" role="img" aria-label="Candlelit dinner table" style="background:linear-gradient(135deg,#2a1e18,#a07850)"></div><div><a href="#">Sed eget leo vitae quam acinia egestas</a><div class="meta">March 16th, 2012 11:32 //<br>duoperks // 5 comments</div></div></li>
        <li><div class="pop-thumb" role="img" aria-label="Skydivers against a blue sky" style="background:linear-gradient(135deg,#1e4a8a,#8ab4e0)"></div><div><a href="#">Suspendisse potenti</a><div class="meta">March 16th, 2012 11:32 //<br>duoperks // 5 comments</div></div></li>
        <li><div class="pop-thumb" role="img" aria-label="Bouquet of pink roses" style="background:linear-gradient(135deg,#f4b8cc,#d45a88)"></div><div><a href="#">Aliquam eleifend eros</a><div class="meta">March 16th, 2012 11:32 //<br>duoperks // 5 comments</div></div></li>
      </ul>
    </section>
  </aside>
</div>
<footer class="footer"><span>All rights reserved 2012 © Duoperks</span><span>Terms of service &nbsp; | &nbsp; Privacy Policy</span></footer>
</body>
</html>
```